Website re-design

I have opened a new frozen yogurt store that will eventually expand into fresh juices and smoothies. I have built a website myself and need to have something that better reflects the brand direction I want to go in.

here is the existing site:
http://www.plumhollowa.com

here is our facebook page, which will be changed to reflect the new web design:
https://www.facebook.com/PlumHollowa

Our look and feel direction will be
Fresh, natural/rustic homemade, quirky, fun

Once I have a new website I will re-launch all of our print collateral to fit with this central part of our communication strategy.

Our brand Vision is listed below
At Plum Hollowa our vision is to create a healthy smile in everyday by constantly delivering deep emotional connections with delicious products in a cool environment.
Updates

Reason: Hi Designers, great work so far. I have extended the deadline as I would like the website to be a one page site with pages that follow on from each other. I will respond to you all shortly.

Hi All, thanks so much for your great work so far.  My existing site uses the Orbel theme, but if you think a different theme would better fit the fresh, rustic and fun approach then please submit designs using this theme.  I am happy to go with a completely different look to what I have now.  

I guess when people come to the site I want it to create a appetite that makes them smile.  Some lines for us are:

Deliciously skinny
Putting a smile in your appetite
Super Plum Hollowa

HI Designers I have posted more photos to the brief and an update to the brief to show you what our store looks like.  We use a lot of old window shutters and blackboards to communicate with customers.  The feeling is very warm and rustic.  I would ideally love if this same look and feel carried across to the website.  I am open to any new ideas you may have.

Target Market(s)

My primary target market is females aged 15 - 25 and secondary is females aged 30 to 55. Every single person who tries our product talks about how diferent the flavours are and what we offer. I need to be able to share this with new potential customers who come across our website.

Industry/Entity Type

Communication

Requirements
Must have
• Fresh images of fruit and yogurt and must take a quirky fun approach to all aspects of the site. Buttons and even headers can all have a quirky approach. The name of plum hollowa is supposed to reflect the yogurt is low fat, but also be a bit cheeky.
Nice to have
• Our store design uses a lots of blackboards and shutters on the roof. It would be nice if our website reflected this rustic homemade warm feel. I would love for there to be a continuation of this feel to the site. I have uploaded some images of the store to the brief to show you what type and look and feel we have in the store

```html
<!DOCTYPE html>
<html lang="en">
<head>
<meta charset="utf-8">
<title>Plum Hollowa – Yogurtologists</title>
<link rel="stylesheet" href="https://fonts.googleapis.com/css2?family=Ubuntu:wght@400;500;700&family=Arimo:wght@400;700&display=swap">
<style>
:root{
  --lime:#b1c800;
  --lime-dark:#9ab000;
  --brown:#5b3a12;
  --brown-deep:#4a2e0c;
  --gold:#a8730f;
  --maroon:#7a1212;
  --grey-bg:#e4e4e4;
  --head-bg:#f1f1f1;
  --text:#333;
  --white:#fff;
}
*{margin:0;padding:0;box-sizing:border-box}
html,body{width:995px;height:1200px;overflow:hidden;background:#fff}
body{font-family:"Arimo",Arial,sans-serif;color:var(--text)}
.page{position:relative;width:995px;height:1200px;overflow:hidden}
.abs{position:absolute}

/* header */
.site-header{left:0;top:0;width:995px;height:160px;border-top:3px solid var(--brown);
  background:repeating-linear-gradient(135deg,#f3f3f3 0 6px,#ebebeb 6px 7px);border-bottom:4px solid var(--lime)}
.tagline{left:109px;top:1px;width:777px;height:31px;background:var(--lime);color:var(--white);
  font:700 12px "Ubuntu",sans-serif;display:flex;align-items:center;justify-content:center}
.brand{left:113px;top:51px;width:145px;height:90px;display:flex;align-items:center;gap:6px}
.brand-dot{width:14px;height:14px;border-radius:50%;background:var(--lime);flex:none}
.brand-name{font:700 24px/1 "Ubuntu",sans-serif;color:var(--brown)}
.call{font:500 16px "Ubuntu",sans-serif;color:#444}
.social{display:flex;gap:3px}
.social span{width:26px;height:26px;display:block}
.s1{background:#d9453a}.s2{background:#4f7bb0}.s3{background:#58c0e8}.s4{background:#c9252f}.s5{background:#3b5998}
.nav{display:flex;gap:17px;font:500 13px "Ubuntu",sans-serif;color:var(--lime-dark)}
.nav li{list-style:none;display:flex;align-items:center;gap:5px}
.nav li::before{content:"";width:14px;height:14px;border-radius:50%;border:2px solid #c9d86a;box-sizing:border-box;background:radial-gradient(circle,#c9d86a 0 2px,transparent 3px)}

/* hero */
.hero-copy{left:161px;top:230px;font-family:"Ubuntu",sans-serif}
.hero-now{font:500 31px/1 "Ubuntu",sans-serif;color:var(--brown-deep)}
.hero-now em{font-style:normal;color:var(--gold)}
.hero-line2{font:500 31px/1 "Ubuntu",sans-serif;color:var(--gold);margin-top:-2px}
.hero-stat{font:500 44px/1 "Ubuntu",sans-serif;color:var(--lime);margin-top:10px}
.hero-stat b{font-weight:700;font-size:50px}
.hero-photo{left:516px;top:166px;width:354px;height:325px;
  background:radial-gradient(ellipse at 42% 30%,#d7b99a 0 22%,transparent 40%),radial-gradient(ellipse at 45% 72%,#f2f2f2 0 30%,transparent 55%),#fff}

/* self serve */
.serve{left:0;top:491px;width:995px;height:386px;background:var(--lime)}
.serve h2{position:absolute;left:0;top:20px;width:995px;text-align:center;font:500 22px "Ubuntu",sans-serif;color:var(--white)}
.serve p.lead{position:absolute;left:140px;top:51px;width:715px;text-align:center;font-size:10.5px;line-height:16px;color:#f4f7dc}
.step{top:102px;width:189px;height:263px;background:var(--white);box-shadow:0 1px 3px rgba(0,0,0,.25);text-align:center}
.step-photo{position:absolute;left:15px;top:8px;width:159px;height:150px;background:radial-gradient(ellipse at 50% 55%,#efefef 0 40%,#fff 70%)}
.step-photo.flag{background:radial-gradient(ellipse at 50% 50%,#27408f 0 35%,#fff 65%)}
.step h3{position:absolute;top:168px;width:100%;font:500 14px "Ubuntu",sans-serif;color:var(--maroon)}
.step p{position:absolute;top:185px;left:10px;right:10px;font-size:10.5px;line-height:15.5px;color:#333}
.btn{position:absolute;top:230px;left:47px;width:95px;height:19px;border-radius:5px;background:var(--lime);color:var(--white);font:500 11px/19px "Ubuntu",sans-serif}

/* goodness */
.goodness{left:0;top:877px;width:995px;height:229px;background:repeating-linear-gradient(45deg,#e6e6e6 0 2px,#dedede 2px 3px)}
.goodness h2{position:absolute;top:33px;width:100%;text-align:center;font:400 20.5px "Ubuntu",sans-serif;color:#555}
.benefit{top:74px;width:189px;height:123px;background:var(--white);border-top:3px solid var(--brown);text-align:center}
.benefit h3{margin-top:12px;font:500 14px "Ubuntu",sans-serif;color:var(--maroon)}
.benefit p{margin:3px 10px 0;font-size:10.5px;line-height:13px;color:#333}
.benefit svg{position:absolute;left:81px;bottom:-13px}

/* footer */
.site-footer{left:0;top:1106px;width:995px;height:94px;background:repeating-linear-gradient(90deg,#5e3e17 0 2px,#573812 2px 4px)}
.site-footer .nav{color:var(--white)}
.copyright{font-size:10.5px;color:#eadfcc}
</style>
</head>
<body>
<div class="page">

  <header class="site-header abs">
    <div class="tagline abs">Plum Hollowa our Yogurtologists work to deliver the most delicious and mouth watering yogurts and toppings to delight your tastes buds.</div>
    <div class="brand abs"><span class="brand-dot"></span><span class="brand-name">plum hollowa</span></div>
    <div class="call abs" style="left:582px;top:63px">Call +61 3 9000 4127</div>
    <div class="social abs" style="left:744px;top:58px"><span class="s1"></span><span class="s2"></span><span class="s3"></span><span class="s4"></span><span class="s5"></span></div>
    <ul class="nav abs" style="left:387px;top:107px">
      <li>Home</li><li>About</li><li>Products</li><li>Contact Us</li><li>Franchise</li><li>Careers</li>
    </ul>
  </header>

  <section class="hero">
    <div class="hero-copy abs">
      <div class="hero-now">NOW <em>in-store</em></div>
      <div class="hero-line2">a super plum hollowa</div>
      <div class="hero-stat"><b>97%</b> Sugar Free</div>
      <div class="hero-stat" style="margin-top:8px"><b>98%</b> Fat Free</div>
    </div>
    <div class="hero-photo abs" role="img" aria-label="Swirl of frozen yogurt in a white branded cup with a wooden spoon"></div>
  </section>

  <section class="serve abs">
    <h2>Self Serve Yogurt Eatery</h2>
    <p class="lead">At Plum Hollowa we provide all the ingredients so you can create the yogurt of your choice. We are a self serve yogurt eatery. Our 98% fat free yogurt is packed with live and active cultures that has been shown to fight cholesterol, strengthen the immune system and aid digestion</p>

    <div class="step abs" style="left:109px">
      <div class="step-photo" role="img" aria-label="Cup of plain frozen yogurt"></div>
      <h3>DISPENSE</h3><p>Swirl a cup full of our delicious 98% fat free yogurt</p>
      <div class="btn">Read More</div>
    </div>
    <div class="step abs" style="left:304px">
      <div class="step-photo" role="img" aria-label="Frozen yogurt cup with berries"></div>
      <h3>MIX IT UP</h3><p>Select from a wide range of ingredients at our toppings bar</p>
      <div class="btn">Read More</div>
    </div>
    <div class="step abs" style="left:500px">
      <div class="step-photo" role="img" aria-label="Yogurt cup sitting on a weighing scale"></div>
      <h3>WEIGHT &amp; PAY</h3><p>100 grams costs $2.80</p>
      <div class="btn">Read More</div>
    </div>
    <div class="step abs" style="left:698px">
      <div class="step-photo flag" role="img" aria-label="Pair of flag printed thongs"></div>
      <h3>AUSTRALIAN MADE</h3><p>We source all of our products from Australian suppliers</p>
      <div class="btn">Read More</div>
    </div>
  </section>

  <section class="goodness abs">
    <h2>Our yogurt is packed full of goodness, that helps to promote better health.</h2>
    <div class="benefit abs" style="left:109px">
      <h3>Real Yogurt</h3><p>Probiotics are wonderful live bacteria that can help improve gastrointestinal flora. This aids with digestion as well as improving your immune system.</p>
      <svg width="27" height="27" viewBox="0 0 27 27"><circle cx="13.5" cy="13.5" r="13" fill="#b1c800"/><path d="M7 11h7V7l7 6.5-7 6.5v-4H7z" fill="#fff"/></svg>
    </div>
    <div class="benefit abs" style="left:305px">
      <h3>98% Fat Free</h3><p>Yes that is right 98% fat free, so you can enjoy your daily dose of Plum Hollowa yogurt without worrying too much about your waist line.</p>
      <svg width="27" height="27" viewBox="0 0 27 27"><circle cx="13.5" cy="13.5" r="13" fill="#b1c800"/><path d="M7 11h7V7l7 6.5-7 6.5v-4H7z" fill="#fff"/></svg>
    </div>
    <div class="benefit abs" style="left:501px">
      <h3 style="margin-top:9px">Gluten Free</h3><p>Gluten is a protein found in wheat and other foods. For people who suffer from Celiac disease this protein can cause some very irritating digestive complaints.</p>
      <svg width="27" height="27" viewBox="0 0 27 27"><circle cx="13.5" cy="13.5" r="13" fill="#b1c800"/><path d="M7 11h7V7l7 6.5-7 6.5v-4H7z" fill="#fff"/></svg>
    </div>
    <div class="benefit abs" style="left:697px">
      <h3>Protein Inside</h3><p>Protein is an essential building block for life and is important to all our daily diets. It helps with energy and releases amino acids to produce more protein in the body.</p>
      <svg width="27" height="27" viewBox="0 0 27 27"><circle cx="13.5" cy="13.5" r="13" fill="#b1c800"/><path d="M7 11h7V7l7 6.5-7 6.5v-4H7z" fill="#fff"/></svg>
    </div>
  </section>

  <footer class="site-footer abs">
    <ul class="nav abs" style="left:17px;top:29px">
      <li>Home</li><li>About</li><li>Products</li><li>Contact Us</li><li>Franchise</li><li>Careers</li>
    </ul>
    <div class="copyright abs" style="left:17px;top:56px">Copyright (c)2013 by Plum Hollowa Pty Ltd.&nbsp; Privacy Policy</div>
    <div class="call abs" style="left:640px;top:30px;color:#fff">Call +61 3 9000 4127</div>
    <div class="social abs" style="left:802px;top:27px"><span class="s1"></span><span class="s2"></span><span class="s3"></span><span class="s4"></span><span class="s5"></span></div>
  </footer>

</div>
</body>
</html>
```